Business Card Design Project

KRV Management Consulting, LLC is a management consulting firm focused on improving an organization’s health and wellness while enhancing company performance with an emphasis on winning in the marketplace, profitable growth, team building, culture enablement and innovation.

Industry/Entity Type

Business

```html
<!DOCTYPE html>
<html lang="en">
<head>
<meta charset="utf-8">
<title>KRV Management Consulting – Business Card</title>
<link href="https://fonts.googleapis.com/css2?family=Poppins:wght@400;600;700&display=swap" rel="stylesheet">
<style>
  :root {
    --page-bg: #ffffff;
    --card-bg: #252525;
    --accent: #86c240;
    --ink-dark: #1f1f1f;
    --ink-light: #ffffff;
  }
  * { margin: 0; padding: 0; box-sizing: border-box; }
  html, body {
    width: 1200px; height: 720px; overflow: hidden;
    background: var(--page-bg);
    font-family: "Poppins", Arial, sans-serif;
  }
  .card {
    position: absolute; left: 36px; top: 36px;
    width: 1125px; height: 646px;
    background: var(--card-bg);
    border-radius: 86px;
    overflow: hidden;
  }
  .identity { position: absolute; left: 41px; top: 272px; }
  .identity__name {
    color: var(--accent); font-weight: 700; font-size: 44px;
    line-height: 1.1; letter-spacing: 0.5px; text-transform: uppercase;
  }
  .identity__role {
    color: var(--ink-light); font-weight: 400; font-size: 31px; line-height: 1.3;
  }
  .contact-band {
    position: absolute; left: 578px; width: 560px; height: 98px;
    background: var(--accent); color: var(--ink-dark);
  }
  .contact-band--phone { top: 130px; }
  .contact-band--web { top: 271px; }
  .contact-band--address { top: 416px; }
  .contact-band__icon { position: absolute; left: 10px; top: 50%; transform: translateY(-50%); }
  .contact-band__lines {
    position: absolute; left: 76px; top: 50%; transform: translateY(-50%);
    font-size: 31px; line-height: 49px; white-space: nowrap;
  }
  .contact-band--phone .contact-band__lines { font-weight: 600; font-size: 33px; }
  .contact-band--web .contact-band__lines { left: 82px; font-size: 30px; }
  .contact-band--address .contact-band__lines { left: 78px; font-size: 30px; line-height: 47px; }
</style>
</head>
<body>
  <div class="card">
    <div class="identity">
      <h1 class="identity__name">Ryan Cole</h1>
      <p class="identity__role">Creative Director</p>
    </div>

    <div class="contact-band contact-band--phone">
      <svg class="contact-band__icon" width="52" height="86" viewBox="0 0 52 86" aria-hidden="true">
        <rect x="4" y="3" width="44" height="80" rx="9" fill="none" stroke="#1f1f1f" stroke-width="5"/>
        <line x1="5" y1="16" x2="47" y2="16" stroke="#1f1f1f" stroke-width="4"/>
        <line x1="5" y1="68" x2="47" y2="68" stroke="#1f1f1f" stroke-width="4"/>
      </svg>
      <div class="contact-band__lines">
        <p>712 4408 193</p>
        <p>836 2571 904</p>
      </div>
    </div>

    <div class="contact-band contact-band--web">
      <svg class="contact-band__icon" width="64" height="54" viewBox="0 0 64 54" aria-hidden="true">
        <rect x="3" y="3" width="58" height="48" fill="none" stroke="#1f1f1f" stroke-width="5"/>
        <polyline points="4,5 32,30 60,5" fill="none" stroke="#1f1f1f" stroke-width="5" stroke-linejoin="round"/>
      </svg>
      <div class="contact-band__lines">
        <p>ryan@krvmanagement.co.in</p>
        <p>www.krvmanagement.com</p>
      </div>
    </div>

    <div class="contact-band contact-band--address">
      <svg class="contact-band__icon" width="66" height="76" viewBox="0 0 66 76" aria-hidden="true">
        <polygon points="33,4 62,34 48,34 48,72 18,72 18,34 4,34" fill="none" stroke="#1f1f1f" stroke-width="5" stroke-linejoin="miter"/>
      </svg>
      <div class="contact-band__lines">
        <p>208, 3rd Floor, Elm Road,</p>
        <p>NY-730145</p>
      </div>
    </div>
  </div>
</body>
</html>
```